Invitation Design Project

In May 2014, my husband and I celebrate our 10th wedding anniversary, and in June 2014 I celebrate my 40th birthday. We will be having a "10/40" party in June 2014 for both events.

This party will be held on my property, "Tallowmere Farm" in North Queensland, so the invitation needs to be fun, whimsical and reflective of both our farm and the Australian bush. You can see photos of our property on facebook: https://www.plinkspace.example/tallowmerefarm

The party will be held on 7 June 2014, RSVP by 1 April 2014.

Target Market(s)

Our family and friends - all ages and backgrounds

Industry/Entity Type

Wedding

Requirements
Must have
• Must have the following details: (wording is flexible)
- Wendy & Martin celebrate their 10th wedding anniversary on 8 May 2014.
- Wendy turns 40 on 9 June 2014
- Party to be held on Tallowmere Farm, 6pm start. Dinner, entertainment and courtesy bus provided, BYO drinks.
- RSVP by 1 April 2014
Must have correct spelling and grammar on the first draft please.
Nice to have
• It might be fun if the invitation could include our pets (dogs, cats, goats, pigs, chickens, parrakeet - see pictures on the facebook link above) in some way, in cartoon form in the background maybe?
Should not have
• I'm not particularly interested in having our photos incorporated into the invitation.

```html
<!DOCTYPE html>
<html lang="en">
<head>
<meta charset="utf-8">
<title>Wendy &amp; Martin – 10/40 Party Invitation</title>
<link rel="stylesheet" href="https://fonts.googleapis.com/css2?family=Philosopher:ital,wght@0,400;0,700;1,400&display=swap">
<style>
  :root {
    --backdrop: #2b2b2b;
    --paper-light: #dcbf83;
    --paper-mid: #cfaa6a;
    --paper-edge: #a86a3a;
    --ink: #4a2a10;
    --ink-soft: #5a3818;
    --art-sepia: #8a6a44;
    --art-sepia-light: #b89868;
    --grass-dark: #5e5a26;
    --grass-light: #8d8a3c;
  }
  * { margin: 0; padding: 0; box-sizing: border-box; }
  html, body {
    width: 1079px;
    height: 1200px;
    overflow: hidden;
    background: var(--backdrop);
  }
  .invitation {
    position: absolute;
    left: 143px;
    top: 40px;
    width: 792px;
    height: 1120px;
    background:
      radial-gradient(ellipse at 50% 40%, var(--paper-light) 0%, var(--paper-mid) 65%, var(--paper-edge) 130%);
    color: var(--ink);
    font-family: "Philosopher", sans-serif;
    text-align: center;
    overflow: hidden;
  }
  .line {
    position: absolute;
    left: 0;
    width: 100%;
    line-height: 1;
    white-space: nowrap;
  }
  .line sup { font-size: 0.5em; vertical-align: 0.8em; }
  .hosts { top: 146px; font-size: 50px; font-weight: 700; }
  .request { top: 198px; font-size: 23px; color: var(--ink-soft); }
  .occasion { top: 302px; font-size: 29px; font-weight: 700; }
  .date { top: 413px; font-size: 28px; }
  .date .day { font-weight: 700; }
  .time { top: 465px; font-size: 24px; }
  .venue { top: 566px; font-size: 32px; line-height: 1.15; }
  .details { top: 750px; font-size: 25px; line-height: 1.35; }
  .rsvp { top: 853px; font-size: 27px; font-style: italic; }

  .ornament, .divider, .illustration, .grass {
    position: absolute;
  }
  .ornament {
    background: radial-gradient(circle, var(--ink-soft) 0%, rgba(90,56,24,0.55) 45%, transparent 72%);
  }
  .ornament-top { left: 346px; top: 8px; width: 100px; height: 100px; }
  .ornament-bottom { left: 358px; top: 898px; width: 76px; height: 72px; }

  .divider {
    height: 18px;
    border-radius: 9px;
    background: linear-gradient(90deg, transparent 0%, rgba(74,42,16,0.7) 12%, var(--ink) 50%, rgba(74,42,16,0.7) 88%, transparent 100%);
  }
  .divider-one { left: 236px; top: 259px; width: 320px; }
  .divider-two { left: 246px; top: 357px; width: 300px; }
  .divider-wide { left: 96px; top: 520px; width: 600px; height: 24px; }
  .divider-short { left: 226px; top: 667px; width: 340px; height: 22px; }

  .illustration {
    border-radius: 40% 40% 12% 12%;
    background: radial-gradient(ellipse at 50% 55%, var(--art-sepia) 0%, var(--art-sepia-light) 55%, transparent 78%);
  }
  .art-goats { left: 612px; top: 604px; width: 180px; height: 126px; }
  .art-rooster { left: 0; top: 878px; width: 214px; height: 172px; }
  .art-cow { left: 540px; top: 925px; width: 216px; height: 152px; }

  .grass {
    left: 0;
    bottom: 0;
    width: 100%;
    height: 72px;
    background: linear-gradient(180deg, transparent 0%, var(--grass-light) 45%, var(--grass-dark) 100%);
  }
</style>
</head>
<body>
  <main class="invitation">
    <div class="ornament ornament-top" role="img" aria-label="Decorative damask flourish"></div>

    <h1 class="line hosts">Wendy &amp; Martin</h1>
    <p class="line request">request the honour of your presence at their</p>

    <div class="divider divider-one" role="img" aria-label="Scrolled flourish divider"></div>
    <p class="line occasion">10<sup>th</sup> wedding anniversary and Wendy’s 40<sup>th</sup> birthday</p>
    <div class="divider divider-two" role="img" aria-label="Scrolled flourish divider"></div>

    <p class="line date">on <span class="day">Saturday</span> the 7th of June 2014</p>
    <p class="line time">at 6:00 in the afternoon</p>

    <div class="divider divider-wide" role="img" aria-label="Wide scrolled flourish divider"></div>
    <p class="line venue">Tallowmere Farm<br>in North Queensland</p>
    <div class="divider divider-short" role="img" aria-label="Scrolled flourish divider"></div>

    <div class="illustration art-goats" role="img" aria-label="Vintage engraving of two goats resting"></div>

    <p class="line details">Dinner, entertainment and courtesy bus provided,<br>BYO drinks</p>
    <p class="line rsvp">RSVP by 1<sup>st</sup> of April 2014</p>

    <div class="ornament ornament-bottom" role="img" aria-label="Small decorative damask flourish"></div>

    <div class="illustration art-rooster" role="img" aria-label="Vintage engraving of a rooster and hen pecking"></div>
    <div class="illustration art-cow" role="img" aria-label="Vintage engraving of a cow standing in a field"></div>
    <div class="grass" role="img" aria-label="Band of grass along the bottom edge"></div>
  </main>
</body>
</html>
```